Email Template for AI Website Builder Marketing Campaign

Update: All the designs submitted have too much content for an email template. I have attached a mockup example of a simplified design. Please follow this guideline to revise your design to be less "wordy" and have less content to optimize the delivery rate of the emails. I have also attached the images I used to create the mockup. Feel free to use these images for your revised designs.
Original Brief:
I need a catchy email template for my new AI Website Builder, WebQuilt.ai. The template must be professional, colorful, yet not too complex. The concept of the product is this:
WebQuilt uses Artificial Intelligence (AI) to instantly build stunning websites, absolutely FREE. The user simply specifies their business name and business category (industry), and their stunning new website appears before their eyes!
The template will be used in MailChimp, so please provide the code that I can simply paste into the email body.
Here is a screenshot of our new website (which is not online yet) so you can match the color scheme and style of the email template to the new website design:
https://pixbinstore.com/art_img/7310582/2208634/48165027/9qrt41hwk826zlmpb3nqd7wyex_image.jpg
Let me know if you have any questions.
Thanks!
All submitted designs are too lengthy (too much content) for an email template. I will provide a mockup showing a sample of how you can simplify your design to function better as an email template and better suit my needs. I appreciate your patience!

```html
<!DOCTYPE html>
<html lang="en">
<head>
<meta charset="UTF-8">
<title>WebQuilt – Email Template</title>
<link rel="stylesheet" href="https://fonts.googleapis.com/css2?family=Jost:wght@300;400;500;600;700&display=swap">
<style>
  :root {
    --navy: #071c33;
    --navy-deep: #041226;
    --navy-mid: #0b3257;
    --cyan: #2ec4f5;
    --blue: #1a9cf0;
    --sky: #33c6f6;
    --page: #edf4fb;
    --card: #eef5fd;
    --ink: #0b1a2a;
    --white: #ffffff;
  }
  * { margin: 0; padding: 0; box-sizing: border-box; }
  html, body { width: 1200px; height: 2250px; overflow: hidden; }
  body {
    font-family: "Jost", "Helvetica Neue", Arial, sans-serif;
    background: var(--page);
    color: var(--ink);
    position: relative;
  }

  /* ---------- Hero ---------- */
  .hero { position: absolute; left: 0; top: 0; width: 1200px; height: 640px; }
  .hero-shape { position: absolute; inset: 0; }
  .hero-art {
    position: absolute; left: 0; top: 0; width: 1200px; height: 610px;
    background:
      radial-gradient(circle at 60px 300px, rgba(46,196,245,.22), transparent 200px),
      radial-gradient(circle at 1010px 160px, rgba(46,196,245,.18), transparent 320px);
  }
  .brand {
    position: absolute; left: 0; width: 1200px;
    display: flex; align-items: center; justify-content: center; gap: 16px;
    font-weight: 600; color: var(--white); letter-spacing: .5px;
  }
  .brand-mark { width: 40px; height: 40px; border-radius: 8px; background: var(--blue); }
  .hero .brand { top: 38px; font-size: 58px; }
  .hero-title {
    position: absolute; top: 190px; left: 0; width: 1200px; text-align: center;
    color: var(--white); font-size: 56px; line-height: 70px; font-weight: 300;
  }
  .hero-title strong { font-weight: 600; display: block; }
  .btn {
    position: absolute; display: flex; align-items: center; justify-content: center;
    font-weight: 500; text-decoration: none; color: var(--white); border-radius: 5px;
  }
  .btn-hero {
    left: 405px; top: 450px; width: 390px; height: 75px; font-size: 25px;
    background: linear-gradient(90deg, #2bc1f5, #1596ef);
  }
  .ai-badge {
    position: absolute; left: 58px; top: 490px; width: 140px; height: 125px;
    border-radius: 18px;
    background: linear-gradient(135deg, #36d0f8, #1a6fe8);
    opacity: .85;
  }

  /* ---------- Steps ---------- */
  .steps-eyebrow {
    position: absolute; top: 694px; left: 0; width: 1200px; text-align: center;
    color: var(--cyan); font-size: 32px; font-weight: 400;
  }
  .steps-title {
    position: absolute; top: 738px; left: 0; width: 1200px; text-align: center;
    font-size: 42px; font-weight: 400; color: var(--ink);
  }
  .steps-text {
    position: absolute; top: 818px; left: 100px; width: 1000px; text-align: center;
    font-size: 32px; line-height: 44px; font-weight: 300; color: #1b2735;
  }
  .features { position: absolute; top: 999px; left: 60px; display: flex; gap: 30px; }
  .feature {
    width: 247px; height: 277px; background: var(--card); border-radius: 6px;
    position: relative; overflow: hidden;
    box-shadow: 0 6px 18px rgba(20,60,110,.08);
  }
  .feature-top { position: absolute; top: 0; left: 0; width: 247px; height: 120px; }
  .feature-icon {
    position: absolute; left: 63px; top: 30px; width: 120px; height: 120px;
    border-radius: 50%; background: var(--white); border: 2px solid var(--cyan);
    display: flex; align-items: center; justify-content: center;
  }
  .feature-label {
    position: absolute; top: 173px; left: 0; width: 247px; text-align: center;
    font-size: 29px; line-height: 36px; font-weight: 500; color: var(--ink);
  }

  /* ---------- Call to action ---------- */
  .cta { position: absolute; left: 0; top: 1350px; width: 1200px; height: 500px; overflow: hidden; }
  .cta-shape { position: absolute; inset: 0; }
  .cta-visual {
    position: absolute; left: 640px; top: 10px; width: 560px; height: 490px;
    background:
      radial-gradient(ellipse at 45% 50%, rgba(120,220,255,.55), transparent 60%),
      linear-gradient(90deg, rgba(51,198,246,0) 0%, #0f5c8f 45%, #062544 100%);
  }
  .cta-kicker {
    position: absolute; left: 123px; top: 118px; font-size: 43px; font-weight: 300; color: var(--white);
  }
  .cta-title {
    position: absolute; left: 123px; top: 170px; font-size: 43px; font-weight: 500; color: var(--navy);
  }
  .cta-text {
    position: absolute; left: 123px; top: 237px; width: 580px;
    font-size: 28px; line-height: 37px; font-weight: 400; color: var(--white);
  }
  .btn-cta {
    left: 123px; top: 346px; width: 240px; height: 75px; font-size: 26px;
    background: var(--navy); border-radius: 4px;
  }

  /* ---------- Footer ---------- */
  .footer {
    position: absolute; left: 0; top: 1845px; width: 1200px; height: 405px;
    background: radial-gradient(ellipse at 50% 30%, #0d3559, var(--navy-deep) 75%);
  }
  .footer .brand { top: 50px; font-size: 52px; }
  .footer .brand-mark { width: 36px; height: 36px; }
  .footer-links {
    position: absolute; top: 155px; left: 0; width: 1200px;
    display: flex; justify-content: center; gap: 52px;
    list-style: none; color: var(--white); font-size: 26px; font-weight: 400;
  }
  .footer-links .sep { opacity: .9; }
  .social {
    position: absolute; top: 233px; left: 231px;
    display: flex; gap: 15px; list-style: none;
  }
  .social li { width: 60px; height: 60px; border-radius: 50%; border: 2px solid var(--white); }
  .social li span {
    display: block; width: 14px; height: 14px; margin: 21px auto; border-radius: 50%;
    background: var(--white);
  }
  .copyright {
    position: absolute; top: 332px; left: 0; width: 1200px; text-align: center;
    font-size: 26px; color: var(--white);
  }
  .copyright span { color: var(--cyan); }
</style>
</head>
<body>

<header class="hero">
  <svg class="hero-shape" width="1200" height="640" viewBox="0 0 1200 640" aria-hidden="true">
    <defs>
      <linearGradient id="heroDark" x1="0" y1="0" x2="1" y2="1">
        <stop offset="0" stop-color="#0a2440"/>
        <stop offset="1" stop-color="#041226"/>
      </linearGradient>
    </defs>
    <path d="M0 0H1200V395C1200 545 1118 627 950 628H0Z" fill="var(--blue)"/>
    <path d="M0 0H1200V372C1192 520 1110 605 950 614H0Z" fill="url(#heroDark)"/>
  </svg>
  <div class="hero-art" role="img" aria-label="Dark blue circuit board and digital network background"></div>

  <div class="brand"><span class="brand-mark"></span>WebQuilt</div>

  <h1 class="hero-title">Let Artificial Intelligence<strong>Buil Your Stunning Website</strong>instantly</h1>

  <a class="btn btn-hero" href="#">Build Free Website Now</a>

  <div class="ai-badge" role="img" aria-label="Stylised AI letters in glowing blue"></div>
</header>

<section class="steps">
  <p class="steps-eyebrow">How you create website with AI</p>
  <h2 class="steps-title">The system gathers some input:</h2>
  <p class="steps-text">Company name business type, location, and color scheme, and the AI gathers text and images to a professionalster</p>

  <div class="features">
    <div class="feature">
      <svg class="feature-top" viewBox="0 0 247 120" aria-hidden="true">
        <defs><linearGradient id="cardTop" x1="0" x2="1"><stop offset="0" stop-color="#33c6f6"/><stop offset="1" stop-color="#1596ef"/></linearGradient></defs>
        <path d="M0 0H247V120C210 120 200 60 123 60S36 120 0 120Z" fill="url(#cardTop)"/>
      </svg>
      <div class="feature-icon">
        <svg width="60" height="66" viewBox="0 0 60 66" fill="none" stroke="#0b1a2a" stroke-width="2.5" stroke-linecap="round" stroke-linejoin="round" aria-hidden="true">
          <rect x="20" y="4" width="26" height="44" rx="4"/><line x1="29" y1="42" x2="37" y2="42"/>
          <path d="M20 30L10 40V60H30L36 50"/><line x1="28" y1="14" x2="38" y2="24" stroke="var(--cyan)"/>
        </svg>
      </div>
      <p class="feature-label">Mobile<br>Focused</p>
    </div>
    <div class="feature">
      <svg class="feature-top" viewBox="0 0 247 120" aria-hidden="true"><path d="M0 0H247V120C210 120 200 60 123 60S36 120 0 120Z" fill="url(#cardTop)"/></svg>
      <div class="feature-icon">
        <svg width="66" height="58" viewBox="0 0 66 58" fill="none" stroke="#0b1a2a" stroke-width="2.5" stroke-linejoin="round" aria-hidden="true">
          <rect x="2" y="2" width="62" height="54" rx="3"/><line x1="2" y1="10" x2="64" y2="10"/>
          <rect x="8" y="16" width="30" height="18" stroke="var(--cyan)"/>
          <line x1="44" y1="18" x2="58" y2="18"/><line x1="44" y1="24" x2="58" y2="24"/><line x1="44" y1="30" x2="58" y2="30"/>
          <rect x="8" y="40" width="14" height="11"/><rect x="26" y="40" width="14" height="11"/><rect x="44" y="40" width="14" height="11"/>
        </svg>
      </div>
      <p class="feature-label">Flexible<br>Use</p>
    </div>
    <div class="feature">
      <svg class="feature-top" viewBox="0 0 247 120" aria-hidden="true"><path d="M0 0H247V120C210 120 200 60 123 60S36 120 0 120Z" fill="url(#cardTop)"/></svg>
      <div class="feature-icon">
        <svg width="62" height="62" viewBox="0 0 62 62" fill="none" stroke="#0b1a2a" stroke-width="2.5" stroke-linejoin="round" aria-hidden="true">
          <rect x="2" y="2" width="58" height="58" rx="3"/><line x1="2" y1="11" x2="60" y2="11"/>
          <rect x="10" y="22" width="42" height="16" stroke="var(--cyan)"/>
          <text x="31" y="34" text-anchor="middle" font-family="Jost, sans-serif" font-size="11" fill="var(--cyan)" stroke="none">FREE</text>
          <line x1="10" y1="46" x2="40" y2="46"/><line x1="10" y1="52" x2="30" y2="52"/>
        </svg>
      </div>
      <p class="feature-label">Free to<br>Try</p>
    </div>
    <div class="feature">
      <svg class="feature-top" viewBox="0 0 247 120" aria-hidden="true"><path d="M0 0H247V120C210 120 200 60 123 60S36 120 0 120Z" fill="url(#cardTop)"/></svg>
      <div class="feature-icon">
        <svg width="66" height="62" viewBox="0 0 66 62" fill="none" stroke="#0b1a2a" stroke-width="2.5" stroke-linejoin="round" aria-hidden="true">
          <path d="M14 24A9 9 0 0 1 16 7 14 14 0 0 1 42 6 11 11 0 0 1 54 24Z"/>
          <rect x="12" y="30" width="42" height="8" rx="2"/><rect x="12" y="41" width="42" height="8" rx="2"/><rect x="12" y="52" width="42" height="8" rx="2"/>
          <line x1="34" y1="10" x2="34" y2="20" stroke="var(--cyan)"/>
        </svg>
      </div>
      <p class="feature-label">Cloud<br>Strenght</p>
    </div>
  </div>
</section>

<section class="cta">
  <svg class="cta-shape" width="1200" height="500" viewBox="0 0 1200 500" aria-hidden="true">
    <defs>
      <linearGradient id="ctaFill" x1="0" x2="1"><stop offset="0" stop-color="#33c6f6"/><stop offset="1" stop-color="#2ab4ee"/></linearGradient>
    </defs>
    <rect width="1200" height="500" fill="var(--page)"/>
    <path d="M0 500V230C0 90 110 2 250 0H1200V500Z" fill="var(--navy)"/>
    <path d="M0 500V260C10 120 110 30 260 22H1200V500Z" fill="url(#ctaFill)"/>
  </svg>
  <div class="cta-visual" role="img" aria-label="Glowing blue digital human head built from circuitry"></div>
  <svg class="cta-shape" width="1200" height="500" viewBox="0 0 1200 500" aria-hidden="true">
    <path d="M1000 500C1110 485 1190 400 1200 270V500Z" fill="var(--sky)"/>
  </svg>

  <p class="cta-kicker">Stop Waiting. Start Building.</p>
  <h2 class="cta-title">Try For Free Now!</h2>
  <p class="cta-text">Lorem Ipsum is simply dummy text of the printing and typesetting industry.</p>
  <a class="btn btn-cta" href="#">Get Started</a>
</section>

<footer class="footer">
  <div class="brand"><span class="brand-mark"></span>WebQuilt</div>
  <ul class="footer-links">
    <li>Terms and Conditions</li><li class="sep">|</li>
    <li>Privacy Policy</li><li class="sep">|</li>
    <li>FAQ</li><li class="sep">|</li>
    <li>Contact Us</li>
  </ul>
  <ul class="social" aria-label="Social channels">
    <li><span></span></li><li><span></span></li><li><span></span></li>
    <li><span></span></li><li><span></span></li><li><span></span></li>
    <li><span></span></li><li><span></span></li><li><span></span></li>
  </ul>
  <p class="copyright">© 2023 <span>WebQuilt</span>. All Rights Reserved</p>
</footer>

</body>
</html>
```